The project is a book cover for a health/recipe book for both Kindle and a future soft cover. Title is Morning Garden Table: Gather Greens and Steady Your Days with a subtitle Six Weeks of Gentle Kitchen Habits. I am a registed dietitian nutritionist specializing in midlife and senior women to help them look and feel 10 years younger by balancing hormones and curbing inflammationI like the idea of fresh colorful whole foods on the cover with a natural clean look. But I am also open to a cover which expresses vitality--perhaps a woman or couple whose "being" expresses energy and vitality.Since I am unsure right at this moment the exact # of pages for the book, I will need to have some wiggle room in the final stages to get the spine dimensions.I am happy to send a table of contents if that would help.I need to decide on a cover in the next 2 weeks. Below are some ideas on style that I like with reservations. Background on 1 is too dark, 2 is too pastel and 3 is good but doesn't move me as much and my followers liked it the least
Updates
Entered wrong completion date and would like more entries.
Target Market(s)
Woman 40 to 65+, college educated
Industry/Entity Type
Nutrition
Colors
Designer to choose colors to be used in the design.
Look and feel
Each slider illustrates characteristics of the customer's brand and the style your logo design should communicate.

```html
<!DOCTYPE html>
<html lang="en">
<head>
<meta charset="utf-8">
<title>Morning Garden Table — Book Cover</title>
<link rel="stylesheet" href="https://fonts.googleapis.com/css2?family=Arvo:wght@700&family=Libre+Baskerville&display=swap">
<style>
  :root {
    --wood-light: #f4f4f3;
    --wood-mid: #e4e5e4;
    --title-red: #a52226;
    --ink-brown: #4a403d;
    --band-lime: #d6e05a;
    --band-ink: #2b2622;
    --plate-white: #eef0ef;
  }
  html, body {
    margin: 0;
    padding: 0;
    overflow: hidden;
    background: #ffffff;
  }
  .cover {
    position: relative;
    width: 800px;
    height: 1200px;
    overflow: hidden;
    background: linear-gradient(180deg, var(--wood-light) 0%, var(--wood-mid) 100%);
  }
  .food-art {
    position: absolute;
    inset: 0;
  }
  .tagline {
    position: absolute;
    top: 178px;
    left: 0;
    width: 100%;
    padding-left: 96px;
    box-sizing: border-box;
    text-align: center;
    font-family: "Arvo", Georgia, serif;
    font-weight: 700;
    font-size: 25px;
    letter-spacing: 0.5px;
    color: var(--ink-brown);
    text-transform: uppercase;
    margin: 0;
  }
  .title {
    position: absolute;
    top: 232px;
    left: 0;
    width: 100%;
    padding-left: 16px;
    box-sizing: border-box;
    margin: 0;
    text-align: center;
    font-family: "Libre Baskerville", Georgia, serif;
    font-weight: 400;
    color: var(--title-red);
    line-height: 1;
  }
  .title-word {
    display: block;
    font-size: 82px;
    letter-spacing: 1px;
  }
  .title-joiner {
    display: block;
    font-size: 40px;
    margin: 8px 0 6px;
  }
  .title-word.last {
    font-size: 118px;
  }
  .subtitle {
    position: absolute;
    top: 548px;
    left: 0;
    width: 100%;
    padding-left: 16px;
    box-sizing: border-box;
    margin: 0;
    text-align: center;
    font-family: "Arvo", Georgia, serif;
    font-weight: 700;
    font-size: 38px;
    line-height: 42px;
    color: var(--ink-brown);
  }
  .subtitle .amp {
    font-size: 26px;
  }
  .brand-band {
    position: absolute;
    left: 0;
    bottom: 0;
    width: 800px;
    height: 62px;
    background: var(--band-lime);
    display: flex;
    align-items: center;
    justify-content: center;
    font-family: "Libre Baskerville", Georgia, serif;
    font-size: 26px;
    letter-spacing: 0.5px;
    color: var(--band-ink);
    text-transform: uppercase;
  }
</style>
</head>
<body>
<div class="cover">
  <svg class="food-art" width="800" height="1200" viewBox="0 0 800 1200" xmlns="http://www.w3.org/2000/svg">
    <defs>
      <radialGradient id="lettuceTone" cx="40%" cy="40%" r="60%">
        <stop offset="0%" stop-color="#a8d36a"/>
        <stop offset="100%" stop-color="#5f9a34"/>
      </radialGradient>
      <radialGradient id="scatterTone" cx="50%" cy="50%" r="55%">
        <stop offset="0%" stop-color="#cfe0b4" stop-opacity="0.9"/>
        <stop offset="100%" stop-color="#e9b2a6" stop-opacity="0"/>
      </radialGradient>
      <radialGradient id="greensTone" cx="50%" cy="50%" r="55%">
        <stop offset="0%" stop-color="#4e8a36"/>
        <stop offset="100%" stop-color="#9cc06a"/>
      </radialGradient>
      <radialGradient id="peachTone" cx="45%" cy="45%" r="60%">
        <stop offset="0%" stop-color="#d5664f"/>
        <stop offset="100%" stop-color="#4f7d33"/>
      </radialGradient>
      <radialGradient id="pepperTone" cx="45%" cy="45%" r="60%">
        <stop offset="0%" stop-color="#f1a23a"/>
        <stop offset="100%" stop-color="#d9452a"/>
      </radialGradient>
    </defs>

    <g role="img" aria-label="Head of fresh butter lettuce">
      <ellipse cx="70" cy="70" rx="150" ry="140" fill="url(#lettuceTone)"/>
    </g>

    <g role="img" aria-label="Scattered salad ingredients with tomatoes, cucumber, peppers and herbs on forks">
      <ellipse cx="690" cy="100" rx="130" ry="115" fill="url(#scatterTone)"/>
    </g>

    <g role="img" aria-label="White plate of mixed green salad with edible flowers and olive oil">
      <circle cx="416" cy="900" r="248" fill="var(--plate-white)"/>
      <ellipse cx="400" cy="910" rx="170" ry="160" fill="url(#greensTone)"/>
    </g>

    <g role="img" aria-label="Peach salad with red onion, almonds and greens">
      <circle cx="120" cy="1004" r="216" fill="#e7b39c"/>
      <circle cx="116" cy="1010" r="196" fill="url(#peachTone)"/>
    </g>

    <g role="img" aria-label="Plate of roasted sweet peppers, mushrooms and eggplant">
      <circle cx="664" cy="1008" r="172" fill="#ffffff"/>
      <circle cx="670" cy="1012" r="150" fill="url(#pepperTone)"/>
    </g>
  </svg>

  <p class="tagline">Six Weeks of Gentle Kitchen Habits</p>

  <h1 class="title">
    <span class="title-word">MORNING</span>
    <span class="title-joiner">garden</span>
    <span class="title-word last">TABLE</span>
  </h1>

  <p class="subtitle">Gather Greens<br><span class="amp">&amp;</span> Steady Your Days</p>

  <div class="brand-band">Good Plate Nutrition</div>
</div>
</body>
</html>
```